We need (2) 4"X4" product label designs for the front and back of an RTU hose on bottle (see attached examples) for a brand new, first-of-its-kind, Aloe Vera product (VerdaKin "The Supreme Root Tonic") specially formulated for agriculture. Most people are aware of the medicinal benefits of aloe vera, however, most people are unaware that it can be used as a soil amendment (organic fertilizer) for plants and lawns, as well as many other crops. This product is for the consumer market. There are about 15 elements that need to go on the front label (which I will provide moving forward), and the backside provides instructions and other relevant information about the product. I will provide a range of examples on the next step of this project.

Need extra days to review

```html
<!DOCTYPE html>
<html lang="en">
<head>
<meta charset="UTF-8">
<title>VerdaKin – The Supreme Root Tonic – Front Label</title>
<link href="https://fonts.googleapis.com/css2?family=Poppins:wght@800&family=Roboto+Condensed:wght@300;700&display=swap" rel="stylesheet">
<style>
  :root {
    --leaf-green: #00843d;
    --deep-green: #00693a;
    --forest-green: #0b5a33;
    --sun-yellow: #fff200;
    --white: #ffffff;
    --ink-grey: #4a4a4a;
    --page: #ffffff;
  }
  html, body {
    margin: 0;
    padding: 0;
    width: 1061px;
    height: 1200px;
    overflow: hidden;
    background: var(--page);
  }
  .canvas {
    position: relative;
    width: 1061px;
    height: 1200px;
  }
  .label {
    position: absolute;
    left: 60px;
    top: 130px;
    width: 940px;
    height: 940px;
    box-sizing: border-box;
    border: 13px solid var(--sun-yellow);
    overflow: hidden;
  }
  .label-art {
    position: absolute;
    inset: 0;
    width: 914px;
    height: 914px;
    display: block;
  }
  .brand-name {
    position: absolute;
    left: 0;
    width: 914px;
    top: 178px;
    margin: 0;
    text-align: center;
    font-family: "Poppins", sans-serif;
    font-weight: 800;
    font-size: 178px;
    line-height: 1;
    letter-spacing: -4px;
    color: var(--white);
  }
  .tagline {
    position: absolute;
    left: 94px;
    top: 354px;
    width: 720px;
    height: 74px;
    box-sizing: border-box;
    background: var(--white);
    border-radius: 14px;
    box-shadow: 4px 4px 0 var(--sun-yellow);
    display: flex;
    align-items: center;
    justify-content: center;
    font-family: "Poppins", sans-serif;
    font-weight: 800;
    font-size: 43px;
    color: var(--forest-green);
    letter-spacing: -0.5px;
  }
  .feature {
    position: absolute;
    top: 661px;
    display: flex;
    align-items: center;
    gap: 22px;
  }
  .feature--organic { left: 162px; }
  .feature--soil { left: 511px; }
  .feature-icon {
    width: 82px;
    height: 82px;
    flex: none;
  }
  .feature-text {
    font-family: "Roboto Condensed", sans-serif;
    font-weight: 300;
    font-size: 38px;
    line-height: 36px;
    color: var(--ink-grey);
  }
  .volume {
    position: absolute;
    left: 0;
    width: 914px;
    top: 852px;
    text-align: center;
    font-family: "Roboto Condensed", sans-serif;
    font-weight: 700;
    font-size: 36px;
    color: var(--white);
  }
</style>
</head>
<body>
<main class="canvas">
  <section class="label">
    <svg class="label-art" viewBox="0 0 914 914" aria-hidden="true">
      <defs>
        <radialGradient id="field" cx="50%" cy="45%" r="70%">
          <stop offset="0" stop-color="#009a46"/>
          <stop offset="1" stop-color="#006336"/>
        </radialGradient>
        <linearGradient id="turf" x1="0" y1="0" x2="1" y2="0">
          <stop offset="0" stop-color="#0a6a35"/>
          <stop offset="0.5" stop-color="#00964a"/>
          <stop offset="1" stop-color="#0a6a35"/>
        </linearGradient>
      </defs>
      <rect class="label-field" width="914" height="914" fill="url(#field)"/>
      <path class="lower-panel" d="M0,657 Q457,477 914,657 L914,914 L0,914 Z" fill="#ffffff"/>
      <path class="sun-arc" d="M0,657 Q457,477 914,657" fill="none" stroke="#fff200" stroke-width="18"/>
    </svg>
    <svg class="label-art" viewBox="0 0 914 914" role="img" aria-label="Grass illustration along the bottom of the label">
      <rect x="0" y="782" width="914" height="132" fill="url(#turf)"/>
    </svg>

    <h1 class="brand-name">VerdaKin</h1>
    <div class="tagline">The Supreme Root Tonic</div>

    <div class="feature feature--organic">
      <svg class="feature-icon" viewBox="0 0 82 82" role="img" aria-label="Sprout and soil icon">
        <circle cx="41" cy="41" r="37" fill="#ffffff" stroke="#0b5a33" stroke-width="6"/>
      </svg>
      <div class="feature-text">Organic<br>Fertilizer</div>
    </div>

    <div class="feature feature--soil">
      <svg class="feature-icon" viewBox="0 0 82 82" role="img" aria-label="Seedling in soil icon">
        <circle cx="41" cy="41" r="37" fill="#ffffff" stroke="#0b5a33" stroke-width="6"/>
      </svg>
      <div class="feature-text">Soil<br>Amendment</div>
    </div>

    <div class="volume">500ml</div>
  </section>
</main>
</body>
</html>
```